Tidecrest NZ Brand, Revenue, Promotions & Events

I need an innovative business card that pops my brand. I like the colours against darker gradients and i'm not afraid to be bold.

I run my own Business, Brand, Event & Promotion company. I specialise in breathing life into businesses and adding atmosphere to promotions and events. I am concept based lady that likes to test the boundaries and create stand out campaigns that connect with the consumer.

I have 12 years business experience in a realm of interesting fields form 11 years in coordinating international music festivals & promotions, 6 years in radio with 8 radio awards including a NZ radio award for best sales team in NZ and was the national brand and sales manager for New Zealands 1st indoor entertainment mall. With 10 years of experience in advertising sales, I have an eye for creating revenue streams for businesses and thrive on implementing campaigns that compliment those streams.

I love sayings like "Do what you love, love what you do" and believe that you can achieve anything you want.

I have been fortunate in my career that my connections have carried me without needing to promote my business however it is important that I start to do so.

Target Market(s)

Decision makers 25 to 54

Contact Information for Business Card

Petra Ollingham
Director
p. 022 587 3091
e. petra@tidecrest.nz
www.tidecrest.nz

FB, IG and Linkedin logo

Font styles to use
Sans Serif

Colors

Designer to choose colors to be used in the design.

Requirements
Must have
• Petra Ollingham
• Director
• p. 022 587 3091
• e. petra@tidecrest.nz
• www.tidecrest.nz
• FB, IG and Linkedin logo
Nice to have
• I am looking for a business card with character, that leaves my presence with my customer and makes them remember my brand & optimistic personality when i walk out the door.

```html
<!DOCTYPE html>
<html lang="en">
<head>
<meta charset="utf-8">
<title>Tidecrest NZ — Business Card</title>
<link href="https://fonts.googleapis.com/css2?family=Montserrat:wght@400;500;600;700&family=Arimo:wght@400&display=swap" rel="stylesheet">
<style>
  :root {
    --brand-blue: #1eaae2;
    --charcoal-dark: #333333;
    --charcoal-light: #636363;
    --ink-grey: #555555;
    --paper: #ffffff;
    --edge: #222222;
  }
  * { box-sizing: border-box; margin: 0; padding: 0; }
  html, body {
    width: 1200px; height: 1200px; overflow: hidden;
    background: var(--paper);
  }
  .canvas { position: relative; width: 1200px; height: 1200px; }

  .card {
    position: absolute; left: 240px; width: 720px; height: 440px;
    border: 1px solid var(--edge);
    box-shadow: 10px 12px 14px rgba(0,0,0,0.22);
    overflow: hidden;
  }

  /* Front */
  .card-front {
    top: 139px;
    background: linear-gradient(90deg, var(--charcoal-dark), var(--charcoal-light));
  }
  .front-wordmark {
    position: absolute; left: 0; right: 0; top: 172px;
    text-align: center;
    font-family: "Montserrat", sans-serif; font-weight: 600;
    font-size: 60px; letter-spacing: 2px; line-height: 1;
    color: var(--brand-blue);
  }
  .front-tagline {
    position: absolute; left: 0; right: 0; top: 243px;
    text-align: center;
    font-family: "Arimo", sans-serif; font-size: 24px;
    color: var(--paper);
  }

  /* Back */
  .card-back { top: 643px; background: var(--paper); }
  .contact-band {
    position: absolute; left: 0; right: 0; top: 220px; bottom: 0;
    background: var(--brand-blue);
  }
  .back-wordmark {
    position: absolute; left: 38px; top: 76px;
    font-family: "Montserrat", sans-serif; font-weight: 600;
    font-size: 42px; letter-spacing: 1.5px; line-height: 1;
    color: var(--brand-blue);
  }
  .back-tagline {
    position: absolute; left: 38px; top: 126px;
    font-family: "Arimo", sans-serif; font-size: 17px;
    color: var(--ink-grey);
  }
  .person-name {
    position: absolute; left: 51px; top: 247px;
    font-family: "Montserrat", sans-serif; font-weight: 700;
    font-size: 32px; color: var(--ink-grey); line-height: 1;
  }
  .person-role {
    position: absolute; left: 51px; top: 280px;
    font-family: "Montserrat", sans-serif; font-weight: 400;
    font-size: 22px; color: var(--paper); line-height: 1;
  }
  .contact-list { position: absolute; left: 49px; top: 318px; list-style: none; }
  .contact-item {
    display: flex; align-items: center; height: 30px; margin-bottom: 2px;
    font-family: "Montserrat", sans-serif; font-weight: 700; font-size: 19px;
    color: var(--paper);
  }
  .contact-item:last-child { margin-top: -4px; }
  .contact-item svg, .contact-item .web-mark { width: 22px; margin-right: 12px; flex: none; }
  .web-mark { font-size: 22px; font-weight: 700; text-align: center; color: var(--paper); }
  .contact-web { color: var(--ink-grey); }

  .social-links {
    position: absolute; left: 525px; top: 366px;
    display: flex; gap: 10px;
  }
  .social-tile {
    width: 34px; height: 34px; border-radius: 6px;
    background: var(--paper);
  }
</style>
</head>
<body>
<div class="canvas">

  <section class="card card-front" aria-label="Card front">
    <div class="front-wordmark">TIDECREST NZ</div>
    <p class="front-tagline">BRAND | REVENUE | EVENTS &amp; PROMOTIONS</p>
  </section>

  <section class="card card-back" aria-label="Card back">
    <div class="contact-band"></div>
    <div class="back-wordmark">TIDECREST NZ</div>
    <p class="back-tagline">BRAND | REVENUE | EVENTS &amp; PROMOTIONS</p>

    <h1 class="person-name">Petra Ollingham</h1>
    <p class="person-role">Director</p>

    <ul class="contact-list">
      <li class="contact-item">
        <svg viewBox="0 0 22 26" height="26" aria-hidden="true">
          <rect x="3" y="1.5" width="16" height="23" rx="3" fill="none" stroke="#fff" stroke-width="2.5"/>
          <circle cx="11" cy="20.5" r="1.4" fill="#fff"/>
        </svg>
        022 587 3091
      </li>
      <li class="contact-item">
        <svg viewBox="0 0 24 18" height="18" aria-hidden="true">
          <rect x="1.2" y="1.2" width="21.6" height="15.6" fill="none" stroke="#fff" stroke-width="2"/>
          <path d="M1.5 1.5 L12 10 L22.5 1.5 M1.5 16.5 L9 8.5 M22.5 16.5 L15 8.5" fill="none" stroke="#fff" stroke-width="2"/>
        </svg>
        petra@tidecrest.nz
      </li>
      <li class="contact-item contact-web">
        <span class="web-mark">W</span>
        www.tidecrest.nz
      </li>
    </ul>

    <div class="social-links" aria-label="Social media profiles">
      <span class="social-tile" role="img" aria-label="Social profile link"></span>
      <span class="social-tile" role="img" aria-label="Social profile link"></span>
      <span class="social-tile" role="img" aria-label="Social profile link"></span>
    </div>
  </section>

</div>
</body>
</html>
```